Check-up reminder postcard

We require a design for a postcard to remind patients to book their dental check up.

Size: standard postcard 100 x 150mm

We are a small family-focussed dental practice. The design should reflect our brand which is warm & sophisticated as well as incorporate the logo colours. For more information please see our website corrindalefamilydental.com.au.

Target Market(s)

Female aged 30 - 45 years old

Industry/Entity Type

Dental

Requirements
Must have
• The front side should have the copy "We've been missing you...".

Back side of postcard should have area for patient name, address, stamp to be placed. The following copy should be used:

"Dear (please leave space for name)

We've been missing you!

We haven't seen you for your regular dental check up. Please call or visit our website to schedule an appointment. Alternatively, we will be in touch over the next couple of weeks.

We look forward to seeing you again soon!

The Corrindale Family Dental team

Phone: 03 9417 2058 Address: 58 Quenby Parade, Corrindale VIC 3162 Web: www.corrindalefamilydental.com.au Email: admin@corrindalefamilydental.com.au"

Include the logo on back side of postcard. Please add the tag line under the logo "Creating beautiful smiles everyday" - sans serif font.

- Design file:
All colours must be converted to CMYK.
Bleed 3mm external from trim.
Trims and registration marks are offset 5mm.
All text to be 3mm from trim if possible.
Nice to have
• Maple leaf as in the logo
Slightly cursive font
Less cluttered look
Should not have
• Cartoons
Pictures of teeth, drills, probes, mirrors
Photos of people

```html
<!DOCTYPE html>
<html lang="en">
<head>
<meta charset="utf-8">
<title>Corrindale Family Dental – Check-up Reminder Postcard</title>
<link rel="stylesheet" href="https://fonts.googleapis.com/css2?family=Goudy+Bookletter+1911&display=swap">
<style>
  :root {
    --olive: #a0aa22;
    --ink: #5b5a4f;
    --teal: #1f8a89;
    --stamp: #e9e8c9;
    --rule: #c9ccb4;
    --paper: #ffffff;
  }
  html, body {
    margin: 0;
    padding: 0;
    width: 1200px;
    height: 799px;
    overflow: hidden;
    background: var(--paper);
  }
  .postcard {
    position: relative;
    width: 1200px;
    height: 799px;
    background: var(--paper);
    font-family: "Goudy Bookletter 1911", Georgia, serif;
    color: var(--olive);
    font-variant-numeric: lining-nums;
  }
  .line {
    position: absolute;
    left: 55px;
    margin: 0;
    font-size: 27px;
    line-height: 40px;
    white-space: nowrap;
  }
  .greeting { top: 52px; }
  .body-copy { line-height: 43px; }
  .copy-missing { top: 134px; }
  .copy-touch { top: 231px; }
  .copy-forward { top: 374px; }
  .signoff { top: 475px; left: 109px; color: var(--ink); }
  .contact-label { top: 561px; }
  .contact-phone {
    top: 606px;
    font-size: 43px;
    line-height: 52px;
    color: var(--ink);
  }
  .contact-web { top: 673px; color: var(--ink); }
  .divider {
    position: absolute;
    left: 621px;
    top: 37px;
    width: 1px;
    height: 731px;
    background: var(--rule);
  }
  .stamp-box {
    position: absolute;
    left: 1003px;
    top: 40px;
    width: 160px;
    height: 200px;
    background: var(--stamp);
  }
  .address-lines {
    position: absolute;
    left: 669px;
    top: 310px;
    width: 476px;
    height: 334px;
  }
  .brand {
    position: absolute;
    right: 40px;
    top: 688px;
    display: flex;
    align-items: center;
    gap: 12px;
  }
  .brand-dot {
    width: 34px;
    height: 34px;
    border-radius: 50%;
    background: var(--olive);
    margin-top: 30px;
  }
  .brand-name {
    font-size: 29px;
    line-height: 33px;
    color: var(--teal);
    text-align: right;
  }
</style>
</head>
<body>
  <main class="postcard">
    <p class="line greeting">Dear</p>
    <p class="line body-copy copy-missing">We've been missing you as we haven't<br>seen you for your dental check up.</p>
    <p class="line body-copy copy-touch">Over the next couple of weeks we will be<br>in touch otherwise, please call or visit our<br>website to book an appointment.</p>
    <p class="line body-copy copy-forward">We look forward to seeing you again<br>soon!</p>
    <p class="line signoff">The Corrindale Family Dental team</p>
    <p class="line contact-label">Call when your free:</p>
    <p class="line contact-phone">03 9417 2058</p>
    <p class="line contact-web">www.corrindalefamilydental.com.au</p>

    <div class="divider"></div>

    <div class="stamp-box"></div>

    <svg class="address-lines" viewBox="0 0 476 334" aria-hidden="true">
      <g stroke="#c9ccb4" stroke-width="1.3">
        <line x1="0" y1="1" x2="476" y2="1"/>
        <line x1="0" y1="56" x2="476" y2="56"/>
        <line x1="0" y1="111" x2="476" y2="111"/>
        <line x1="0" y1="166" x2="476" y2="166"/>
        <line x1="0" y1="221" x2="476" y2="221"/>
        <line x1="0" y1="276" x2="476" y2="276"/>
        <line x1="0" y1="331" x2="476" y2="331"/>
      </g>
    </svg>

    <div class="brand">
      <div class="brand-dot"></div>
      <div class="brand-name">Corrindale<br>Family Dental</div>
    </div>
  </main>
</body>
</html>
```